New Web Design Project

www.tessaridgeservices.com - this is the current site, the logo has been designed but everything needs to be upgraded to give it a more professional look. Use your creative talent to come up with something visually appeal and professional for this Law web-site

```html
<!DOCTYPE html>
<html lang="en">
<head>
<meta charset="utf-8">
<title>Tessaridge Law Services</title>
<link rel="stylesheet" href="https://fonts.googleapis.com/css2?family=Lato:ital,wght@0,400;0,700;0,900;1,400&display=swap">
<style>
:root{
  --red:#d0102a;
  --navy:#0a2a8c;
  --blue:#0d2f9e;
  --ink:#222;
  --text:#333;
  --grey-light:#e8e8e8;
  --grey-mid:#bdbdbd;
  --dark:#2b2f36;
  --white:#fff;
}
*{margin:0;padding:0;box-sizing:border-box}
html,body{width:1200px;height:3644px;overflow:hidden}
body{font-family:'Lato',sans-serif;color:var(--text);background:var(--white);position:relative}
.abs{position:absolute}
.site-header{left:0;top:0;width:1200px;height:88px;background:var(--white);z-index:3}
.brand{left:112px;top:0;width:201px;height:110px;background:var(--white);box-shadow:0 2px 8px rgba(0,0,0,.15);z-index:4;display:flex;flex-direction:column;align-items:center;justify-content:center;gap:6px}
.brand span{font-weight:900;color:var(--navy);font-size:26px;letter-spacing:1px;line-height:1}
.brand small{font-weight:900;color:var(--navy);font-size:12px;letter-spacing:3px}
.brand-square{width:14px;height:14px;background:var(--red)}
.main-nav{top:32px;left:377px;font-size:15px;color:var(--ink);z-index:4}
.main-nav a{position:absolute;white-space:nowrap;color:var(--ink);text-decoration:none}
.main-nav a.active{color:var(--red)}
.active-bar{left:372px;top:0;width:58px;height:5px;background:var(--navy);z-index:4}
.phone{left:940px;top:29px;font-size:17px;color:var(--ink);z-index:4}
.hero{left:0;top:88px;width:1200px;height:588px;background:linear-gradient(180deg,#5f7fa0 0%,#3f5672 45%,#2a3542 100%)}
.hero-title{top:296px;width:1200px;text-align:center;color:var(--white);font-size:42px;font-weight:700;letter-spacing:.3px;line-height:56px}
.hero-sub{top:357px;width:1200px;text-align:center;color:var(--white);font-size:22px;font-weight:700}
.btn-red{background:var(--red);color:var(--white);font-weight:700;text-align:center;font-size:18px;display:flex;align-items:center;justify-content:center}
.hero-btn{left:515px;top:413px;width:168px;height:44px}
.hero-arrow{top:306px}
.about{top:676px;left:0;width:1200px;height:410px}
.sec-title{width:1200px;text-align:center;font-size:34px;color:var(--ink)}
.sec-title.on-dark{color:var(--white)}
.about-rule{left:457px;top:792px;width:303px;height:1px;background:#999}
.about-mark{left:590px;top:780px;width:20px;height:10px;background:var(--red)}
.about-text{left:221px;top:820px;width:779px;text-align:center;font-size:15px;line-height:26px;color:var(--text)}
.about-text p{margin-bottom:14px}
.services{left:0;top:1086px;width:1200px;height:530px;background:linear-gradient(135deg,#0c2a93,#0a1f74)}
.notch{left:570px;top:1086px}
.service-card{top:1193px;width:234px;height:345px;border:1px solid rgba(255,255,255,.55);text-align:center;color:var(--white)}
.service-card h3{position:absolute;top:146px;width:100%;font-size:16px;line-height:20px;font-weight:900;text-transform:uppercase}
.service-card p{position:absolute;top:196px;left:18px;right:18px;font-size:13px;line-height:19px}
.service-card svg{position:absolute;left:69px;top:22px}
.testimonials-title{top:1660px;width:1200px;text-align:center;font-size:28px;color:var(--red)}
.quote-card{top:1718px;width:291px;height:175px;background:var(--white);box-shadow:0 2px 10px rgba(0,0,0,.18)}
.quote-card p{position:absolute;left:55px;top:26px;right:36px;font-style:italic;font-size:13px;line-height:24px;color:#999}
.quote-mark{position:absolute;left:22px;top:22px;font-size:48px;color:var(--navy);font-weight:900;line-height:1}
.author{top:1918px;display:flex;align-items:center;gap:14px}
.avatar{width:48px;height:48px;border-radius:50%;background:#b9a58c}
.author b{display:block;font-size:14px;color:var(--ink)}
.author i{font-style:normal;font-size:12px;color:#888}
.t-arrow{top:1790px}
.split{left:0;top:2048px;width:1200px;height:397px}
.split-text h2{font-size:30px;font-weight:400;color:var(--white);letter-spacing:.5px}
.split-text p{font-size:16px;line-height:24px;color:var(--white);margin-top:12px}
.btn-outline{display:inline-flex;width:152px;height:44px;border:2px solid var(--white);color:var(--white);align-items:center;justify-content:center;font-weight:700;font-size:17px;margin-top:26px}
.map{left:0;top:2445px;width:1200px;height:362px;background:linear-gradient(135deg,#cfcfcf,#a9a9a9)}
.contact{left:0;top:2807px;width:1200px;height:469px;background:linear-gradient(180deg,#3a3f47,#23262b)}
.field{color:var(--white);font-size:17px;border-bottom:1px solid rgba(255,255,255,.8);padding-bottom:10px}
.footer{left:0;top:3276px;width:1200px;height:304px;background:var(--grey-light)}
.foot-brand{left:117px;top:3330px;width:250px;height:130px;display:flex;flex-direction:column;align-items:center;justify-content:center;gap:8px}
.foot-brand span{font-weight:900;color:var(--navy);font-size:32px;letter-spacing:1px}
.foot-brand small{font-weight:900;color:var(--navy);font-size:14px;letter-spacing:4px}
.foot-col{top:3330px}
.foot-col h4{font-size:20px;font-weight:700;color:var(--ink);margin-bottom:14px;letter-spacing:.5px}
.foot-col li{list-style:none;font-size:14px;color:#555;line-height:30px}
.social{top:3375px;width:42px;height:42px;border:2px solid var(--red);border-radius:50%}
.bottom-bar{left:0;top:3580px;width:1200px;height:64px;background:var(--grey-mid);text-align:center;line-height:64px;font-size:14px;color:#444}
</style>
</head>
<body>

<header class="abs site-header"></header>
<div class="abs active-bar"></div>
<div class="abs brand"><div class="brand-square"></div><span>TESSARIDGE</span><small>LAW SERVICES</small></div>
<nav class="abs main-nav">
  <a class="active" style="left:0">HOME</a>
  <a style="left:80px">ABOUT US</a>
  <a style="left:185px">SERVICES</a>
  <a style="left:287px">ESTATE PLANNING</a>
  <a style="left:449px">CONTACT</a>
</nav>
<div class="abs phone">+1 555-014-2290</div>

<section class="abs hero" role="img" aria-label="City skyline with skyscrapers beside a lake"></section>
<h1 class="abs hero-title">WELCOME TO TESSARIDGE LAW SERVICES</h1>
<div class="abs hero-sub">MAURIS VEL LACUS VITAE FELIS VESTIBULUM VOLUTPAT</div>
<div class="abs btn-red hero-btn">Learn More</div>
<svg class="abs hero-arrow" style="left:95px" width="24" height="48" viewBox="0 0 24 48"><polyline points="22,2 2,24 22,46" fill="none" stroke="#fff" stroke-width="2"/></svg>
<svg class="abs hero-arrow" style="left:1085px" width="24" height="48" viewBox="0 0 24 48"><polyline points="2,2 22,24 2,46" fill="none" stroke="#fff" stroke-width="2"/></svg>

<section class="abs about"></section>
<h2 class="abs sec-title" style="top:728px">ABOUT TESSARIDGE</h2>
<div class="abs about-rule"></div>
<div class="abs about-mark"></div>
<div class="abs about-text">
  <p>I came to the United States in 2005 and I was thrown into a world of chaos, learning how to deal with issues such as immigration, taxes, and housing. As I spent more time in the states, it became clear that the US is very complicated for expats with the myriad of rules and regulations that an expat has to navigate.</p>
  <p>It is my belief that by passing on my knowledge and experience, I can help expats and international investors, be better prepared and have the support they need, to successfully navigate the system. That is why my entire focus is on expats and international clients. I have a variety of resources and relationships that go beyond the legal advice I provide, to help my clients in other areas of their lives.</p>
</div>

<section class="abs services"></section>
<svg class="abs notch" width="60" height="26" viewBox="0 0 60 26"><polygon points="0,0 60,0 30,26" fill="#fff"/></svg>
<h2 class="abs sec-title on-dark" style="top:1130px;font-size:30px">OUR SERVICES</h2>

<div class="abs service-card" style="left:121px">
  <svg width="96" height="108" viewBox="0 0 96 108"><polygon points="48,2 94,28 94,80 48,106 2,80 2,28" fill="#d0102a" stroke="#fff" stroke-width="2"/><rect x="30" y="38" width="36" height="32" fill="none" stroke="#fff" stroke-width="3"/><line x1="30" y1="48" x2="66" y2="48" stroke="#fff" stroke-width="3"/></svg>
  <h3>Estate<br>Planning</h3>
  <p>While no one enjoys thinking about death or disability, establishing an estate plan is one of the most important steps you can take to protect yourself and your loved ones.</p>
</div>
<div class="abs service-card" style="left:364px">
  <svg width="96" height="108" viewBox="0 0 96 108"><polygon points="48,2 94,28 94,80 48,106 2,80 2,28" fill="#d0102a" stroke="#fff" stroke-width="2"/><path d="M48 74 L30 56 A10 10 0 0 1 48 42 A10 10 0 0 1 66 56 Z" fill="none" stroke="#fff" stroke-width="3"/><path d="M44 56h8M48 52v8" stroke="#fff" stroke-width="3"/></svg>
  <h3>Long-Term Care &amp;<br>Medicaid</h3>
  <p>The high cost of long-term care has made planning a critically important issue for most middle-class seniors and their families.</p>
</div>
<div class="abs service-card" style="left:607px">
  <svg width="96" height="108" viewBox="0 0 96 108"><polygon points="48,2 94,28 94,80 48,106 2,80 2,28" fill="#d0102a" stroke="#fff" stroke-width="2"/><rect x="34" y="36" width="28" height="38" fill="none" stroke="#fff" stroke-width="3"/><path d="M40 44h4M52 44h4M40 52h4M52 52h4M40 60h4M52 60h4" stroke="#fff" stroke-width="3"/></svg>
  <h3>Real Estate<br>Services</h3>
  <p>It can be quite difficult for expats to avoid all real estate risk when dealing with an unfamiliar market. I strive to provide my clients with all they may need to finalize</p>
</div>
<div class="abs service-card" style="left:850px">
  <svg width="96" height="108" viewBox="0 0 96 108"><polygon points="48,2 94,28 94,80 48,106 2,80 2,28" fill="#d0102a" stroke="#fff" stroke-width="2"/><circle cx="48" cy="44" r="8" fill="none" stroke="#fff" stroke-width="3"/><path d="M34 72 Q48 50 62 72" fill="none" stroke="#fff" stroke-width="3"/></svg>
  <h3>Special Needs<br>Planning</h3>
  <p>If you currently support or provide care for a child or loved one with special needs (such as physical and/or mental disabilities), what would you do if you were n</p>
</div>

<h2 class="abs testimonials-title">CLIENT TESTIMONIALS</h2>
<svg class="abs t-arrow" style="left:72px" width="18" height="34" viewBox="0 0 18 34"><polyline points="16,2 2,17 16,32" fill="none" stroke="#888" stroke-width="2"/></svg>
<svg class="abs t-arrow" style="left:1104px" width="18" height="34" viewBox="0 0 18 34"><polyline points="2,2 16,17 2,32" fill="none" stroke="#888" stroke-width="2"/></svg>

<div class="abs quote-card" style="left:124px"><span class="quote-mark">“</span><p>Morbi diam mauris viverra in gravida eu mattis in ante Morbi eget arcu Morbi porta libero id ullamcorper nonummy nibh ligula pulvinar metus eget</p></div>
<div class="abs quote-card" style="left:457px"><span class="quote-mark">“</span><p>Morbi diam mauris viverra in gravida eu mattis in ante Morbi eget arcu Morbi porta libero id ullamcorper nonummy nibh ligula pulvinar metus eget</p></div>
<div class="abs quote-card" style="left:792px"><span class="quote-mark">“</span><p>Morbi diam mauris viverra in gravida eu mattis in ante Morbi eget arcu Morbi porta libero id ullamcorper nonummy nibh ligula pulvinar metus eget</p></div>

<div class="abs author" style="left:134px"><div class="avatar" role="img" aria-label="Client portrait"></div><div><b>By Author Name</b><i>City Location</i></div></div>
<div class="abs author" style="left:467px"><div class="avatar" role="img" aria-label="Client portrait"></div><div><b>By Author Name</b><i>City Location</i></div></div>
<div class="abs author" style="left:802px"><div class="avatar" role="img" aria-label="Client portrait"></div><div><b>By Author Name</b><i>City Location</i></div></div>

<svg class="abs split" width="1200" height="397" viewBox="0 0 1200 397" role="img" aria-label="Red and blue panels over documents and a pen">
  <rect width="1200" height="397" fill="#0d2f9e"/>
  <polygon points="0,0 656,0 462,397 0,397" fill="#d0102a"/>
</svg>
<div class="abs split-text" style="left:134px;top:2145px;width:390px">
  <h2>ESTATE TAX</h2>
  <p>Consider your US Estate Tax and Probate Avoidance and the Impact of the Estate Tax in the Foreign Country of Your Residencea</p>
  <div class="btn-outline">Learn More</div>
</div>
<div class="abs split-text" style="left:663px;top:2145px;width:400px">
  <h2>POWER OF ATTORNEY</h2>
  <p>Many people form a power of attorney specifically for addressing medical concerns. If a person were to become incapacitated for medical reasons</p>
  <div class="btn-outline">Learn More</div>
</div>

<section class="abs map" role="img" aria-label="Street map of the office location"></section>

<section class="abs contact" role="img" aria-label="Desk with laptop and glasses in dim light"></section>
<h2 class="abs sec-title on-dark" style="top:2862px;font-size:30px">CONTACT US</h2>
<div class="abs field" style="left:163px;top:2955px;width:267px">Your Name</div>
<div class="abs field" style="left:467px;top:2955px;width:267px">Email address</div>
<div class="abs field" style="left:770px;top:2955px;width:268px">Phone Number</div>
<div class="abs field" style="left:163px;top:3013px;width:875px;height:97px">Write a message here</div>
<div class="abs btn-red" style="left:505px;top:3149px;width:207px;height:41px">SEND NOW</div>

<footer class="abs footer"></footer>
<div class="abs foot-brand"><span>TESSARIDGE</span><small>LAW SERVICES</small></div>
<div class="abs foot-col" style="left:442px"><h4>QUICK LINKS</h4><ul><li>Home</li><li>About Us</li><li>Why Us</li><li>Our Team</li></ul></div>
<div class="abs foot-col" style="left:649px"><h4>RESOURCES</h4><ul><li>Our Services</li><li>Testimonials</li><li>Support</li><li>Contact Us</li></ul></div>
<div class="abs foot-col" style="left:870px"><h4>FOLLOW US</h4></div>
<div class="abs social" style="left:868px"></div>
<div class="abs social" style="left:914px"></div>
<div class="abs social" style="left:961px"></div>
<div class="abs social" style="left:1009px"></div>
<div class="abs bottom-bar">© 2018 Company Name. All right reserved</div>

</body>
</html>
```